App Design for Diary & Todo Do List Android App

This project is to create a four screen design for Velvo Journal which is a Diary, Journal, Notepad and Todo List App. All information about this design can be found in https://lnkr.example/Qb7TzW
I have also attached same as PDF

Velvo Journal is private Diary, Journal, Notes & Todo List app for professionals and home users. This is to design 4 screens for Velvo Journal Android App and they are:

1. Note List Screen
2. Todo List Screen
3. Task List Screen
4. Add Task Screen

The main goal of this design are

Good user experience
Good app design

Diary app, Notepad app, and Todo List are common app category so the goal of this design is to create a simple, intuitive and elegant design. I have included my own attempt as example in this Google Doc https://lnkr.example/Qb7TzW

Target Market(s)

Brindle App Market

Industry/Entity Type

Android

Font styles to use
Serif
Sans Serif
Script

Colors

Designer to choose colors to be used in the design.

Requirements
Must have
• Elegant and intuitive design that makes it easy for people to add and complete Todo List tasks and enter journal.
Nice to have
• New app icon
Should not have
• N/A

```html
<!DOCTYPE html>
<html lang="en">
<head>
<meta charset="utf-8">
<title>Velvo Journal – Notes</title>
<link rel="stylesheet" href="https://fonts.googleapis.com/css2?family=Source+Sans+3:wght@400;600;700&display=swap">
<style>
  :root {
    --green-dark: #4aa800;
    --green-light: #78d200;
    --green-fab: #4fae0a;
    --page-bg: #ffffff;
    --list-bg: #f7f8f8;
    --rail: #d6d6d6;
    --ink: #3a3a3a;
    --ink-soft: #474747;
    --blue: #2aa7e2;
    --yellow: #f1c232;
    --red: #e0342c;
    --teal: #26d0cc;
    --tab-green: #8fd13f;
    --tab-green-dark: #3d9e0c;
  }
  * { box-sizing: border-box; margin: 0; padding: 0; }
  html, body { width: 1000px; height: 1200px; overflow: hidden; background: var(--page-bg); }
  body { font-family: "Source Sans 3", sans-serif; color: var(--ink); position: relative; }

  .screen {
    position: absolute; left: 172px; top: 18px;
    width: 570px; height: 1012px;
    transform: scale(1.15); transform-origin: 0 0;
    background: var(--list-bg); overflow: hidden;
    box-shadow: 0 0 0 1px #e6e6e6;
  }

  .app-bar {
    position: absolute; left: 0; top: 0; width: 570px; height: 113px;
    background: linear-gradient(100deg, var(--green-dark) 0%, var(--green-light) 100%);
    color: #fff;
  }
  .status { position: absolute; top: 6px; left: 12px; right: 10px; height: 22px; font-size: 17px; font-weight: 600; }
  .status .signal { position: absolute; left: 0; top: 4px; }
  .status .time { position: absolute; left: 0; right: 0; text-align: center; top: 0; }
  .status .battery { position: absolute; right: 0; top: 0; display: flex; align-items: center; gap: 8px; }
  .app-title { position: absolute; left: 0; right: 0; top: 48px; text-align: center; font-size: 28px; font-weight: 400; }
  .search { position: absolute; left: 510px; top: 51px; }

  .timeline-rail { position: absolute; left: 49px; top: 168px; width: 1px; height: 760px; background: var(--rail); }
  .date-dot { position: absolute; left: 35px; top: 139px; width: 30px; height: 30px; border-radius: 50%; border: 1px solid #cfcfcf; background: #fff; }
  .date-tag {
    position: absolute; left: 87px; top: 137px; width: 135px; height: 40px;
    border: 1px solid var(--green-dark); border-radius: 3px; background: #fff;
    font-size: 16px; color: #555; line-height: 38px; padding-left: 18px;
  }
  .date-tag::before {
    content: ""; position: absolute; left: -7px; top: 13px; width: 12px; height: 12px;
    background: #fff; border-left: 1px solid var(--green-dark); border-bottom: 1px solid var(--green-dark);
    transform: rotate(45deg);
  }

  .entry-icon {
    position: absolute; left: 24px; width: 50px; height: 50px; border-radius: 50%;
    border: 1px solid currentColor; background: #fff;
    display: flex; align-items: center; justify-content: center;
  }
  .card {
    position: absolute; left: 87px; width: 446px; height: 122px;
    border: 1px solid currentColor; border-radius: 4px; background: #fff;
  }
  .card.is-note { color: var(--blue); }
  .card.is-photo { color: var(--yellow); }
  .card.is-pdf { color: var(--red); }
  .card.is-video { color: var(--teal); }
  .card-text { position: absolute; left: 31px; top: 21px; right: 20px; }
  .card.has-thumb .card-text { left: 139px; }
  .card-title { font-size: 20px; font-weight: 600; color: var(--ink); line-height: 26px; letter-spacing: .2px; }
  .card-body { font-size: 15.5px; color: var(--ink-soft); line-height: 22px; margin-top: 3px; }
  .thumb { position: absolute; left: 31px; top: 25px; width: 86px; height: 70px; }
  .thumb.mountain { background: linear-gradient(180deg, #7fa6c8 0%, #8d9a8a 45%, #5d7a3e 75%, #3f6a2a 100%); }
  .thumb.party { background: linear-gradient(135deg, #2a4f8f 0%, #5b8fd0 40%, #b2332f 75%, #2b2b3a 100%); }

  .fab {
    position: absolute; left: 456px; top: 837px; width: 74px; height: 74px; border-radius: 50%;
    background: var(--green-fab); box-shadow: 0 3px 8px rgba(0,0,0,.25);
    display: flex; align-items: center; justify-content: center;
  }

  .tab-bar {
    position: absolute; left: 0; top: 926px; width: 570px; height: 86px; background: #fff;
    box-shadow: 0 -2px 6px rgba(0,0,0,.06); display: flex;
  }
  .tab { flex: 1; display: flex; align-items: center; justify-content: center; }
</style>
</head>
<body>
<main class="screen">
  <header class="app-bar">
    <div class="status">
      <svg class="signal" width="80" height="14" viewBox="0 0 80 14">
        <g fill="#fff"><circle cx="5" cy="7" r="4"/><circle cx="15" cy="7" r="4"/><circle cx="25" cy="7" r="4"/></g>
        <g fill="none" stroke="#fff" stroke-width="1.3"><circle cx="35" cy="7" r="3.6"/><circle cx="45" cy="7" r="3.6"/></g>
        <g fill="none" stroke="#fff" stroke-width="2" stroke-linecap="round">
          <path d="M66 4a10 10 0 0 1 14 0"/><path d="M69 7.5a6 6 0 0 1 8 0"/>
        </g>
        <circle cx="73" cy="11" r="1.8" fill="#fff"/>
      </svg>
      <div class="time">12:00</div>
      <div class="battery">
        <svg width="10" height="16" viewBox="0 0 10 16"><path d="M1 4l8 8-4 3V1l4 3-8 8" fill="none" stroke="rgba(255,255,255,.6)" stroke-width="1.3"/></svg>
        <span>100%</span>
        <svg width="37" height="16" viewBox="0 0 37 16"><rect x="1" y="1" width="32" height="14" rx="2.5" fill="#fff" stroke="#fff"/><rect x="34" y="5" width="2.5" height="6" rx="1" fill="#fff"/></svg>
      </div>
    </div>
    <h1 class="app-title">Notes</h1>
    <svg class="search" width="34" height="34" viewBox="0 0 34 34" aria-label="Search">
      <circle cx="13" cy="13" r="10.5" fill="none" stroke="#fff" stroke-width="2.8"/>
      <path d="M21 21l10 10" stroke="#fff" stroke-width="4" stroke-linecap="round"/>
    </svg>
  </header>

  <div class="timeline-rail"></div>
  <div class="date-dot"></div>
  <div class="date-tag">June 12, 2015</div>

  <!-- note -->
  <div class="entry-icon" style="top:234px;color:var(--blue)">
    <svg width="22" height="26" viewBox="0 0 22 26"><rect x="1" y="1" width="20" height="24" rx="1.5" fill="none" stroke="currentColor" stroke-width="2"/><g stroke="currentColor" stroke-width="2"><path d="M5 7h12M5 11h12M5 15h12M5 19h12"/></g></svg>
  </div>
  <article class="card is-note" style="top:197px">
    <div class="card-text">
      <h2 class="card-title">Name of Notes</h2>
      <p class="card-body">Lorem ipsum dolor sit amet, consectetur adipis<br>cing elit, sed do eiusmod tempor...</p>
    </div>
  </article>

  <!-- photo -->
  <div class="entry-icon" style="top:374px;color:var(--yellow)">
    <svg width="26" height="22" viewBox="0 0 26 22"><rect x="1" y="1" width="24" height="20" rx="1.5" fill="none" stroke="currentColor" stroke-width="2"/><circle cx="8" cy="7" r="2.5" fill="currentColor"/><path d="M3 19l7-7 4 4 4-5 6 8z" fill="currentColor"/></svg>
  </div>
  <article class="card is-photo has-thumb" style="top:337px">
    <div class="thumb mountain" role="img" aria-label="Photo of green mountain peaks under a blue sky"></div>
    <div class="card-text">
      <h2 class="card-title">Name of Photo</h2>
      <p class="card-body">Some photos I took when we hike to the<br>mountain last week</p>
    </div>
  </article>

  <!-- pdf -->
  <div class="entry-icon" style="top:514px;color:var(--red)">
    <svg width="22" height="26" viewBox="0 0 22 26"><path d="M2 1h13l5 5v19H2z" fill="none" stroke="currentColor" stroke-width="2"/><rect x="0" y="15" width="22" height="9" fill="currentColor"/><text x="11" y="22.5" font-family="Source Sans 3, sans-serif" font-size="8" font-weight="700" fill="#fff" text-anchor="middle">PDF</text><path d="M7 12c2-6 3-8 4-4s3 5 5 4" fill="none" stroke="currentColor" stroke-width="1.2"/></svg>
  </div>
  <article class="card is-pdf" style="top:477px">
    <div class="card-text">
      <h2 class="card-title">Name of Pdf</h2>
      <p class="card-body">Lorem ipsum dolor sit amet, consectetur adipis<br>cing elit, sed do eiusmod tempor...</p>
    </div>
  </article>

  <!-- video -->
  <div class="entry-icon" style="top:654px;color:var(--teal)">
    <svg width="28" height="26" viewBox="0 0 28 26"><rect x="0" y="0" width="28" height="26" rx="2" fill="currentColor"/><g fill="#fff"><rect x="2" y="3" width="3" height="3"/><rect x="2" y="9" width="3" height="3"/><rect x="2" y="15" width="3" height="3"/><rect x="2" y="21" width="3" height="3"/><rect x="23" y="3" width="3" height="3"/><rect x="23" y="9" width="3" height="3"/><rect x="23" y="15" width="3" height="3"/><rect x="23" y="21" width="3" height="3"/><rect x="7" y="2" width="14" height="10"/><rect x="7" y="14" width="14" height="10"/></g></svg>
  </div>
  <article class="card is-video has-thumb" style="top:617px">
    <div class="thumb party" role="img" aria-label="Video still of a festive crowd with confetti"></div>
    <div class="card-text">
      <h2 class="card-title">Name of Video</h2>
      <p class="card-body">Some photos I took when we hike to the<br>mountain last week</p>
    </div>
  </article>

  <!-- note -->
  <div class="entry-icon" style="top:794px;color:var(--blue)">
    <svg width="22" height="26" viewBox="0 0 22 26"><rect x="1" y="1" width="20" height="24" rx="1.5" fill="none" stroke="currentColor" stroke-width="2"/><g stroke="currentColor" stroke-width="2"><path d="M5 7h12M5 11h12M5 15h12M5 19h12"/></g></svg>
  </div>
  <article class="card is-note" style="top:757px">
    <div class="card-text">
      <h2 class="card-title">Name of Notes</h2>
      <p class="card-body">Lorem ipsum dolor sit amet, consectetur adipis<br>cing elit, sed do eiusmod tempor...</p>
    </div>
  </article>

  <!-- photo, partly under tab bar -->
  <article class="card is-photo has-thumb" style="top:897px">
    <div class="thumb mountain" role="img" aria-label="Photo of a mountain landscape"></div>
    <div class="card-text">
      <h2 class="card-title">Name of Photo</h2>
    </div>
  </article>

  <div class="fab" aria-label="Add entry">
    <svg width="34" height="34" viewBox="0 0 34 34"><path d="M17 2v30M2 17h30" stroke="#fff" stroke-width="3.5" stroke-linecap="round"/></svg>
  </div>

  <nav class="tab-bar">
    <div class="tab" aria-label="Notes">
      <svg width="42" height="38" viewBox="0 0 42 38"><rect x="12" y="1" width="28" height="30" fill="none" stroke="var(--tab-green-dark)" stroke-width="2.5"/><rect x="7" y="4" width="28" height="30" fill="#fff" stroke="var(--tab-green-dark)" stroke-width="2.5"/><rect x="2" y="8" width="28" height="28" fill="var(--tab-green-dark)"/><rect x="6" y="16" width="9" height="8" fill="#fff"/><g stroke="#fff" stroke-width="2.5"><path d="M18 17h8M18 22h8M6 29h20"/></g></svg>
    </div>
    <div class="tab" aria-label="Todo list">
      <svg width="42" height="38" viewBox="0 0 42 38"><g fill="none" stroke="var(--tab-green)" stroke-width="2.5"><path d="M2 5l3 3 5-6"/><path d="M14 4h26M14 9h18M14 17h26M14 22h18M14 30h26M14 35h18"/></g><circle cx="5" cy="19" r="3" fill="var(--tab-green)"/><circle cx="5" cy="32" r="3" fill="var(--tab-green)"/></svg>
    </div>
    <div class="tab" aria-label="Folders">
      <svg width="44" height="36" viewBox="0 0 44 36"><path d="M1 4h14l4 4h21v26H1z" fill="var(--tab-green)"/><path d="M6 13h37l-5 21H1z" fill="#b6e37e"/></svg>
    </div>
    <div class="tab" aria-label="Settings">
      <svg width="40" height="38" viewBox="0 0 40 38"><g fill="none" stroke="var(--tab-green)" stroke-width="3.5" stroke-dasharray="3.5 2.6"><circle cx="12" cy="19" r="9"/><circle cx="29" cy="10" r="7"/><circle cx="29" cy="29" r="7"/></g><g fill="none" stroke="var(--tab-green)" stroke-width="2"><circle cx="12" cy="19" r="5"/><circle cx="29" cy="10" r="3.5"/><circle cx="29" cy="29" r="3.5"/></g></svg>
    </div>
  </nav>
</main>
</body>
</html>
```